Velmora VIP Golden Ticket postcard design

Velmora is a new massage parlour opening in Manchester England this is a second business for me and I want to create a post card size VIP Golden ticket for our regular customers offering a free glass of champagne with there first service and a discounted rate for the first month it needs to incorporate the address 217b Tessford Vale Road Hinwick Manchester M34 6QJ, telephone number 0161-492-3857.The website address www.Velmorrastudio.example. I want the post card to be gold with the name Velmora in pink the rest of the wording in black where it says free glass of champagne the text needs to be bold. The overall look of the post ccad should communicate glamour and luxury with style and finesse

Massage

```html
<!DOCTYPE html>
<html lang="en">
<head>
<meta charset="utf-8">
<title>Velmora Massage – VIP Golden Ticket</title>
<link rel="stylesheet" href="https://fonts.googleapis.com/css2?family=Open+Sans:wght@400;600;700;800&family=Italianno&family=Pinyon+Script&family=Cormorant+Garamond:wght@500&display=swap">
<style>
  :root {
    --bg-deep: #c39a3c;
    --bg-mid: #dcba66;
    --bg-light: #f1dc9c;
    --swoosh: rgba(255, 248, 225, 0.45);
    --brand-pink: #ee1cb4;
    --ink: #111111;
    --glass-pink: #e05ac4;
    --glass-soft: #f4b5e4;
    --mark-dark: #141414;
  }
  * { margin: 0; padding: 0; box-sizing: border-box; }
  html, body { width: 1200px; height: 930px; overflow: hidden; background: var(--bg-mid); }
  .card {
    position: relative;
    width: 1200px;
    height: 930px;
    overflow: hidden;
    background: linear-gradient(100deg, var(--bg-deep) 0%, var(--bg-mid) 45%, var(--bg-light) 100%);
    font-family: "Open Sans", Arial, sans-serif;
    color: var(--ink);
  }
  .card__swooshes { position: absolute; inset: 0; z-index: 0; }
  .brand-name {
    position: absolute;
    top: 22px;
    left: 0;
    width: 100%;
    text-align: center;
    font-weight: 700;
    font-size: 112px;
    line-height: 1;
    letter-spacing: 6px;
    color: var(--brand-pink);
    z-index: 2;
  }
  .brand-tag {
    position: absolute;
    top: 128px;
    left: 470px;
    font-family: "Italianno", cursive;
    font-size: 108px;
    line-height: 1;
    letter-spacing: 8px;
    color: var(--brand-pink);
    z-index: 2;
  }
  .offer-intro {
    position: absolute;
    top: 314px;
    left: 118px;
    font-weight: 700;
    font-size: 29px;
    letter-spacing: -0.3px;
    z-index: 2;
  }
  .drink-art {
    position: absolute;
    left: 420px;
    top: 388px;
    width: 300px;
    height: 340px;
    z-index: 1;
  }
  .offer-headline {
    position: absolute;
    top: 360px;
    left: 108px;
    font-family: "Pinyon Script", cursive;
    font-size: 112px;
    font-weight: 400;
    line-height: 150px;
    color: var(--ink);
    -webkit-text-stroke: 2px var(--ink);
    z-index: 3;
  }
  .offer-terms {
    position: absolute;
    top: 696px;
    left: 110px;
    font-family: "Cormorant Garamond", Georgia, serif;
    font-weight: 500;
    font-size: 26px;
    line-height: 34px;
    z-index: 2;
  }
  .venue {
    position: absolute;
    left: 740px;
    top: 352px;
    width: 410px;
    text-align: right;
    z-index: 2;
  }
  .venue__mark {
    display: inline-flex;
    align-items: center;
    justify-content: center;
    gap: 14px;
    width: 186px;
    height: 126px;
    margin-right: 58px;
    background: var(--mark-dark);
    font-weight: 700;
    font-size: 26px;
    color: var(--brand-pink);
  }
  .venue__mark-square { width: 16px; height: 16px; background: var(--brand-pink); }
  .venue__address {
    margin-top: 8px;
    font-size: 24px;
    line-height: 32px;
  }
  .venue__phone {
    margin-top: 18px;
    margin-right: 4px;
    display: flex;
    justify-content: flex-end;
    align-items: center;
    gap: 12px;
    font-weight: 700;
    font-size: 28px;
    letter-spacing: 1px;
  }
  .divider {
    position: absolute;
    left: 474px;
    top: 805px;
    width: 248px;
    height: 14px;
    z-index: 2;
  }
  .website {
    position: absolute;
    top: 838px;
    left: 0;
    width: 100%;
    text-align: center;
    font-weight: 700;
    font-size: 29px;
    letter-spacing: 2.2px;
    z-index: 2;
  }
</style>
</head>
<body>
<main class="card">
  <svg class="card__swooshes" width="1200" height="930" viewBox="0 0 1200 930" aria-hidden="true">
    <path d="M0 330 C 250 190, 700 190, 1200 320 L1200 0 L0 0 Z" fill="rgba(255,250,230,0.14)"/>
    <path d="M0 330 C 250 190, 700 190, 1200 320" fill="none" stroke="var(--swoosh)" stroke-width="3"/>
    <path d="M40 0 C 120 120, 260 230, 0 330" fill="none" stroke="var(--swoosh)" stroke-width="2"/>
    <path d="M930 0 C 1020 140, 1120 240, 1200 260" fill="none" stroke="var(--swoosh)" stroke-width="2"/>
    <path d="M600 930 C 850 840, 1050 760, 1200 640" fill="none" stroke="rgba(255,248,225,0.3)" stroke-width="2"/>
    <path d="M820 930 C 980 860, 1120 800, 1200 770" fill="none" stroke="rgba(255,248,225,0.25)" stroke-width="2"/>
  </svg>

  <h1 class="brand-name">VELMORA</h1>
  <p class="brand-tag">Massage</p>

  <p class="offer-intro">THIS CARD ENTITLES YOU TO A</p>

  <svg class="drink-art" viewBox="0 0 300 340" role="img" aria-label="Pink champagne cocktail in a martini glass with a lime slice and splash">
    <defs>
      <radialGradient id="drinkGlow" cx="50%" cy="45%" r="55%">
        <stop offset="0%" stop-color="var(--glass-pink)" stop-opacity="0.8"/>
        <stop offset="60%" stop-color="var(--glass-soft)" stop-opacity="0.4"/>
        <stop offset="100%" stop-color="var(--glass-soft)" stop-opacity="0"/>
      </radialGradient>
    </defs>
    <rect x="0" y="0" width="300" height="340" fill="url(#drinkGlow)"/>
  </svg>

  <h2 class="offer-headline">Free Glass<br>of Champagne</h2>

  <p class="offer-terms">on your first service<br>plus a discounted rate for the first month</p>

  <section class="venue">
    <div class="venue__mark"><span class="venue__mark-square"></span>Velmora</div>
    <p class="venue__address">217b Tessford Vale Road<br>Hinwick, Manchester M34 6QJ</p>
    <p class="venue__phone">
      <svg width="22" height="22" viewBox="0 0 24 24" aria-hidden="true">
        <circle cx="12" cy="12" r="10.5" fill="none" stroke="var(--ink)" stroke-width="2"/>
        <path d="M9 6.5 L10.5 9.5 L9.3 10.7 C10 12.5 11.5 14 13.3 14.7 L14.5 13.5 L17.5 15 L16.5 17.5 C11.5 17.5 6.5 12.5 6.5 7.5 Z" fill="var(--ink)"/>
      </svg>
      0161-492-3857
    </p>
  </section>

  <svg class="divider" viewBox="0 0 248 14" aria-hidden="true">
    <line x1="10" y1="7" x2="238" y2="7" stroke="var(--ink)" stroke-width="1.5"/>
    <rect x="3" y="3" width="8" height="8" transform="rotate(45 7 7)" fill="var(--ink)"/>
    <rect x="237" y="3" width="8" height="8" transform="rotate(45 241 7)" fill="var(--ink)"/>
  </svg>

  <p class="website">www.Velmorrastudio.example</p>
</main>
</body>
</html>
```